Waschkarten-Design für Tankstelle gesucht
Zielgruppe
Unsere Tankstelle hat in eine neue Waschanlage investiert. Die Alten Waschkarten gefallen nicht mehr, und sind auch mit der Programmstruktur nicht mehr kompatibel. Siehe Anhang.
Waschkunden in der Portalwaschanlage jeglichen Alters und Geschlechts.
Aufgabenstellung
Wertigkeit der einzelnen Waschprogramme muss erkennbar sein. Beschriftung z. B. Mehrfachwäschen 3er 5er 10er bzw. Wertkarten der Preis soll veränderbar sein, so das die Karten jederzeit angepasst werden können. Auch sollte der Programm-Name von uns selbst geändert werden können. Die Einschiebe Richtung muss klar erkennbar sein.
Das Design muss im Check-Kartenformat sein. Achtung abgerundete Ecken mit ca. r=2 mm
Anbei ein Bild von unserer Neuen Waschanlage

```html
<!DOCTYPE html>
<html lang="de">
<head>
<meta charset="utf-8">
<title>Waschkarten – Programmübersicht</title>
<link href="https://fonts.googleapis.com/css2?family=Ubuntu:wght@300;400;700&display=swap" rel="stylesheet">
<style>
  :root {
    --frame: #0e4a5c;
    --paper: #ffffff;
    --ink-light: #ffffff;
    --ink-dark: #111111;
    --express: #5b5547;
    --basic: #8d5a27;
    --classic: #4e90c6;
    --top: #9b4e97;
    --glanz: #4f7b37;
    --premium: #f2bc34;
    --photo-dark: #2b2d30;
  }
  * { box-sizing: border-box; margin: 0; padding: 0; }
  html, body { width: 1200px; height: 1200px; overflow: hidden; background: var(--paper); }
  .sheet {
    position: relative;
    width: 1200px; height: 1200px;
    background: var(--paper);
    border: 6px solid var(--frame);
  }
  .wash-card {
    position: absolute;
    width: 502px; height: 317px;
    overflow: hidden;
    font-family: "Ubuntu", sans-serif;
    color: var(--ink-light);
    background: var(--tone);
  }
  .wash-card.col-left { left: 82px; }
  .wash-card.col-right { left: 604px; }
  .wash-card.row-1 { top: 98px; }
  .wash-card.row-2 { top: 435px; }
  .wash-card.row-3 { top: 772px; }
  .wash-card.express { --tone: var(--express); }
  .wash-card.basic { --tone: var(--basic); }
  .wash-card.classic { --tone: var(--classic); }
  .wash-card.top { --tone: var(--top); }
  .wash-card.glanz { --tone: var(--glanz); }
  .wash-card.premium { --tone: var(--premium); }

  .color-panel {
    position: absolute; left: 0; top: 0;
    width: 174px; height: 100%;
    background: linear-gradient(160deg, var(--tone) 0%, color-mix(in srgb, var(--tone) 70%, #000) 100%);
  }
  .machine-photo {
    position: absolute; left: 174px; top: 0;
    width: 328px; height: 100%;
    background:
      linear-gradient(180deg, color-mix(in srgb, var(--tone) 45%, #9aa3a8) 0%, color-mix(in srgb, var(--tone) 35%, var(--photo-dark)) 35%, color-mix(in srgb, var(--tone) 30%, var(--photo-dark)) 100%);
  }
  .program-name {
    position: absolute; left: 22px; top: 30px;
    font-weight: 700; font-size: 71px; line-height: 1;
    letter-spacing: 0.5px;
    text-shadow: 0 3px 10px rgba(0,0,0,0.35);
  }
  .program-desc {
    position: absolute; left: 23px; top: 100px;
    font-weight: 300; font-size: 29px; line-height: 34px;
    text-shadow: 0 2px 6px rgba(0,0,0,0.3);
  }
  .insert-arrow {
    position: absolute; left: 251px; top: 172px;
    width: 236px; height: 131px;
  }
  .price {
    position: absolute; right: 38px; top: 186px;
    font-weight: 300; font-size: 64px; line-height: 1;
    white-space: nowrap;
    text-shadow: 0 2px 8px rgba(0,0,0,0.25);
  }
  .station-mark {
    position: absolute; left: 22px; top: 224px;
    display: flex; align-items: center; gap: 8px;
    color: var(--ink-dark);
    font-weight: 700; font-size: 17px; line-height: 1.1;
  }
  .station-mark .dot {
    width: 18px; height: 18px; border-radius: 50%;
    background: var(--ink-dark);
    flex: none;
  }
</style>
</head>
<body>
<main class="sheet">

  <section class="wash-card express col-left row-1">
    <div class="color-panel"></div>
    <div class="machine-photo" role="img" aria-label="Foto der Portalwaschanlage mit Bürsten vor wolkigem Himmel"></div>
    <h2 class="program-name">EXPRESS</h2>
    <p class="program-desc">Waschen und Trocknen</p>
    <svg class="insert-arrow" viewBox="0 0 236 131" aria-hidden="true"><path d="M0 34H124V0L236 65.5L124 131V97H0Z" fill="#fff" fill-opacity="0.55"/></svg>
    <p class="price">€ 5,95</p>
    <div class="station-mark"><span class="dot"></span><span>Tankstelle<br>Lindner</span></div>
  </section>

  <section class="wash-card basic col-right row-1">
    <div class="color-panel"></div>
    <div class="machine-photo" role="img" aria-label="Foto der Portalwaschanlage mit Bürsten vor wolkigem Himmel"></div>
    <h2 class="program-name">BASIC</h2>
    <p class="program-desc">Schaumwäsche</p>
    <svg class="insert-arrow" viewBox="0 0 236 131" aria-hidden="true"><path d="M0 34H124V0L236 65.5L124 131V97H0Z" fill="#fff" fill-opacity="0.55"/></svg>
    <p class="price">€ 8,95</p>
    <div class="station-mark"><span class="dot"></span><span>Tankstelle<br>Lindner</span></div>
  </section>

  <section class="wash-card classic col-left row-2">
    <div class="color-panel"></div>
    <div class="machine-photo" role="img" aria-label="Foto der Portalwaschanlage mit Bürsten vor wolkigem Himmel"></div>
    <h2 class="program-name">CLASSIC</h2>
    <p class="program-desc">Wachs</p>
    <svg class="insert-arrow" viewBox="0 0 236 131" aria-hidden="true"><path d="M0 34H124V0L236 65.5L124 131V97H0Z" fill="#fff" fill-opacity="0.55"/></svg>
    <p class="price">€ 10,95</p>
    <div class="station-mark"><span class="dot"></span><span>Tankstelle<br>Lindner</span></div>
  </section>

  <section class="wash-card top col-right row-2">
    <div class="color-panel"></div>
    <div class="machine-photo" role="img" aria-label="Foto der Portalwaschanlage mit Bürsten vor wolkigem Himmel"></div>
    <h2 class="program-name">TOP</h2>
    <p class="program-desc">Wachs &amp; Unterboden</p>
    <svg class="insert-arrow" viewBox="0 0 236 131" aria-hidden="true"><path d="M0 34H124V0L236 65.5L124 131V97H0Z" fill="#fff" fill-opacity="0.55"/></svg>
    <p class="price">€ 12,95</p>
    <div class="station-mark"><span class="dot"></span><span>Tankstelle<br>Lindner</span></div>
  </section>

  <section class="wash-card glanz col-left row-3">
    <div class="color-panel"></div>
    <div class="machine-photo" role="img" aria-label="Foto der Portalwaschanlage mit Bürsten vor wolkigem Himmel"></div>
    <h2 class="program-name">GLANZ</h2>
    <p class="program-desc">Politurprogramm</p>
    <svg class="insert-arrow" viewBox="0 0 236 131" aria-hidden="true"><path d="M0 34H124V0L236 65.5L124 131V97H0Z" fill="#fff" fill-opacity="0.55"/></svg>
    <p class="price">€ 14,95</p>
    <div class="station-mark"><span class="dot"></span><span>Tankstelle<br>Lindner</span></div>
  </section>

  <section class="wash-card premium col-right row-3">
    <div class="color-panel"></div>
    <div class="machine-photo" role="img" aria-label="Foto der Portalwaschanlage mit Bürsten vor wolkigem Himmel"></div>
    <h2 class="program-name">PREMIUM</h2>
    <p class="program-desc">Politurprogramm mit<br>Unterbodenwäsche</p>
    <svg class="insert-arrow" viewBox="0 0 236 131" aria-hidden="true"><path d="M0 34H124V0L236 65.5L124 131V97H0Z" fill="#fff" fill-opacity="0.55"/></svg>
    <p class="price">€ 16,95</p>
    <div class="station-mark"><span class="dot"></span><span>Tankstelle<br>Lindner</span></div>
  </section>

</main>
</body>
</html>
```